Stationary for Hair Cosmetic company

We mainly sell hair thickening products www.morvello-wellform.de/morvello-hair/ Hair thickening products are a smart and easy solution for thinning hair for both men and women. We sell very information oriented in an honest undramatic manner.

We would like to see a decent color and style that is suitable for men and women. It shall be rather modern with a vintage spin as our own product (Morvello Bottle). Please use our logo (attatched).

Please bias your design to the bottle. To give you an idea: Chalk design like http://de.pixaverum.com/id/48213597 or one-color watercolor like http://de.pixaverum.com/id/63925180 is appreciated but not necessary.

Good but rejected designs will get compensation.

Target Market(s)

Wide range in demographics: age 20-55; 45% male, 55% women; issues with hair loss; self-conscious

Industry/Entity Type

Hair

Colors
3377b5
33a6d7
32b7a4
cbdf83
fbf289
fee18a
f9bb93
f05157

Requirements
Must have
• trustworthiness
Nice to have
• Chalk design like http://de.pixaverum.com/id/48213597 or one-color watercolor like http://de.pixaverum.com/id/63925180 is appreciated but not necessary

```html
<!DOCTYPE html>
<html lang="en">
<head>
<meta charset="utf-8">
<title>Morvello Hair – Stationery Set</title>
<link rel="stylesheet" href="https://fonts.googleapis.com/css2?family=Source+Sans+3:wght@400;600&display=swap">
<style>
  :root {
    --backdrop: #5b3e2a;
    --paper: #ffffff;
    --ink: #1e1e1e;
    --ink-soft: #555555;
    --rule: #3a3a3a;
    --blue-light: #33a6d7;
    --blue-deep: #3377b5;
    --accent-red: #f05157;
    --mark-faint: #e4e4e4;
    --label: #ffffff;
  }
  * { box-sizing: border-box; margin: 0; padding: 0; }
  html, body { width: 1200px; height: 504px; overflow: hidden; }
  body {
    position: relative;
    background: var(--backdrop);
    font-family: "Source Sans 3", sans-serif;
    color: var(--ink);
  }
  .piece { position: absolute; background: var(--paper); box-shadow: 0 2px 6px rgba(0,0,0,.35); overflow: hidden; }

  /* brand lockup */
  .brand { position: absolute; display: flex; flex-direction: column; align-items: center; }
  .brand-dot { width: 34px; height: 34px; border-radius: 50%; background: var(--ink); }
  .brand-name { margin-top: 5px; font-size: 7px; font-weight: 600; letter-spacing: .12em; text-transform: uppercase; color: var(--ink); white-space: nowrap; }

  .piece-label { position: absolute; color: var(--label); font-size: 24px; font-weight: 400; }

  /* letterhead */
  .letterhead { left: 26px; top: 36px; width: 323px; height: 417px; }
  .letterhead .brand { left: 50%; top: 8px; transform: translateX(-50%); }
  .letterhead-mark { position: absolute; left: 98px; top: 138px; width: 124px; height: 133px; border-radius: 50%; border: 2px solid var(--mark-faint); display: flex; align-items: center; justify-content: center; }
  .letterhead-mark span { font-size: 13px; font-weight: 600; letter-spacing: .12em; text-transform: uppercase; color: var(--mark-faint); }
  .letterhead-footer { position: absolute; left: 0; right: 0; bottom: 8px; text-align: center; font-size: 6.4px; color: var(--ink-soft); line-height: 1.7; }
  .contact-row { display: flex; justify-content: center; gap: 6px; }
  .icon { display: inline-block; width: 5px; height: 5px; border-radius: 50%; background: var(--accent-red); margin-right: 2px; vertical-align: middle; }

  /* fax */
  .fax { left: 386px; top: 36px; width: 321px; height: 417px; }
  .fax .brand { left: 16px; top: 8px; }
  .fax-contact { position: absolute; left: 233px; top: 12px; padding-left: 6px; border-left: 1px solid #bbb; font-size: 6px; line-height: 1.45; color: var(--ink-soft); }
  .fax-title { position: absolute; left: 17px; top: 88px; font-size: 20px; font-weight: 400; }
  .fax-field { position: absolute; height: 10px; border-bottom: 1px solid var(--rule); font-size: 5.5px; color: var(--ink); }
  .fax-field.left { left: 17px; width: 160px; }
  .fax-field.right { left: 180px; width: 111px; }
  .fax-checks { position: absolute; left: 17px; top: 203px; width: 276px; display: flex; justify-content: space-between; font-size: 5.6px; }
  .fax-checks span { display: flex; align-items: center; gap: 4px; }
  .fax-checks i { width: 7px; height: 7px; border: 1px solid var(--ink); }
  .band { position: absolute; left: 0; bottom: 0; }
  .band-url { position: absolute; right: 10px; bottom: 2px; color: #fff; letter-spacing: .06em; font-size: 7.5px; }

  /* envelopes */
  .envelope-back { left: 810px; top: 24px; width: 360px; height: 160px; }
  .envelope-mid { left: 732px; top: 92px; width: 360px; height: 162px; }
  .envelope-front { left: 770px; top: 164px; width: 360px; height: 160px; }
  .flap { position: absolute; left: 0; top: 0; }
  .envelope-back .brand-dot, .envelope-mid .brand-dot { position: absolute; width: 30px; height: 34px; }
  .envelope-front .brand { left: 10px; top: 6px; }

  /* business cards */
  .card-front { left: 762px; top: 358px; width: 188px; height: 107px; }
  .card-front .brand { left: 24px; top: 14px; }
  .card-divider { position: absolute; left: 102px; top: 26px; width: 1px; height: 44px; background: #bbb; }
  .card-info { position: absolute; left: 110px; top: 26px; font-size: 4.6px; line-height: 1.5; color: var(--ink-soft); }
  .card-name { font-size: 6.5px; font-weight: 600; color: var(--accent-red); }
  .card-back { left: 964px; top: 358px; width: 187px; height: 107px; background: var(--blue-light); }
  .card-back .brand-dot { position: absolute; left: 76px; top: 18px; width: 36px; height: 48px; border-radius: 50%; }
  .card-back-url { position: absolute; left: 0; right: 0; top: 87px; text-align: center; font-size: 6px; letter-spacing: .16em; color: #1e4a66; }
</style>
</head>
<body>

<!-- Letterhead -->
<section class="piece letterhead">
  <div class="brand"><div class="brand-dot"></div><div class="brand-name">Morvello Hair</div></div>
  <div class="letterhead-mark"><span>Morvello</span></div>
  <footer class="letterhead-footer">
    <div>Street Name, City Name, Zip Code-00000</div>
    <div class="contact-row">
      <span><i class="icon"></i>012-555-0147</span>
      <span><i class="icon"></i>012-555-0147</span>
      <span><i class="icon"></i>info@morvellowellform.de</span>
      <span><i class="icon"></i>www.morvello-wellform.de</span>
    </div>
  </footer>
</section>
<div class="piece-label" style="left:174px;top:464px;">LH</div>

<!-- Fax sheet -->
<section class="piece fax">
  <div class="brand"><div class="brand-dot"></div><div class="brand-name">Morvello Hair</div></div>
  <div class="fax-contact">
    <div><i class="icon"></i>012-555-0147</div>
    <div><i class="icon"></i>012-555-0147</div>
    <div><i class="icon"></i>info@morvellowellform.de</div>
    <div>Street Name, City Name</div>
    <div>Zip Code-00000</div>
  </div>
  <h1 class="fax-title">FAX</h1>
  <div class="fax-field left" style="top:124px;">To :</div>
  <div class="fax-field right" style="top:124px;">From :</div>
  <div class="fax-field left" style="top:141px;">Fax :</div>
  <div class="fax-field right" style="top:141px;">Pages :</div>
  <div class="fax-field left" style="top:158px;">Phone :</div>
  <div class="fax-field right" style="top:158px;">Date :</div>
  <div class="fax-field left" style="top:175px;">Re :</div>
  <div class="fax-field right" style="top:175px;">CC :</div>
  <div class="fax-checks">
    <span><i></i>Urgent</span><span><i></i>For Review</span><span><i></i>Please Comment</span><span><i></i>Please Reply</span><span><i></i>Please Recycle</span>
  </div>
  <svg class="band" width="321" height="14" viewBox="0 0 321 14">
    <polygon points="0,1 207,1 203,4 0,4" fill="var(--blue-light)"/>
    <polygon points="0,6 205,6 212,0 321,0 321,14 0,14" fill="var(--blue-deep)"/>
  </svg>
  <div class="band-url">www.morvello-wellform.de</div>
</section>
<div class="piece-label" style="left:528px;top:466px;">FAX</div>

<!-- Envelopes -->
<section class="piece envelope-back">
  <svg class="flap" width="360" height="62" viewBox="0 0 360 62">
    <path d="M0,0 H360 L352,14 Q345,20 335,22 L200,60 Q180,64 160,60 L25,22 Q15,20 8,14 Z" fill="var(--blue-light)"/>
  </svg>
  <div class="brand-dot" style="left:165px;top:8px;"></div>
</section>
<section class="piece envelope-mid">
  <svg class="flap" width="360" height="70" viewBox="0 0 360 70">
    <path d="M1,1 H359 L352,16 Q346,22 336,24 L195,62 Q180,66 165,62 L24,24 Q14,22 8,16 Z" fill="#f6f6f6" stroke="#333" stroke-width="1"/>
  </svg>
  <div class="brand-dot" style="left:165px;top:12px;"></div>
</section>
<section class="piece envelope-front">
  <div class="brand"><div class="brand-dot"></div><div class="brand-name">Morvello Hair</div></div>
  <svg class="band" width="360" height="14" viewBox="0 0 360 14">
    <polygon points="0,1 232,1 228,4 0,4" fill="var(--blue-light)"/>
    <polygon points="0,6 230,6 237,0 360,0 360,14 0,14" fill="var(--blue-deep)"/>
  </svg>
  <div class="band-url">www.morvello-wellform.de</div>
</section>

<!-- Business cards -->
<section class="piece card-front">
  <div class="brand"><div class="brand-dot" style="width:40px;height:48px;"></div><div class="brand-name">Morvello Hair</div></div>
  <div class="card-divider"></div>
  <div class="card-info">
    <div class="card-name">Your Name</div>
    <div>Title</div>
    <div style="margin-top:3px;"><i class="icon" style="width:3px;height:3px;"></i>012-555-0147</div>
    <div><i class="icon" style="width:3px;height:3px;"></i>012-555-0147</div>
    <div><i class="icon" style="width:3px;height:3px;"></i>info@morvellowellform.de</div>
    <div style="margin-top:2px;">Street Name, City Name</div>
    <div>Zip Code-00000</div>
  </div>
  <svg class="band" width="188" height="12" viewBox="0 0 188 12">
    <polygon points="0,1 98,1 95,3.5 0,3.5" fill="var(--blue-light)"/>
    <polygon points="0,5 97,5 103,0 188,0 188,12 0,12" fill="var(--blue-deep)"/>
  </svg>
  <div class="band-url" style="font-size:5px;right:8px;bottom:1px;">www.morvello-wellform.de</div>
</section>
<section class="piece card-back">
  <div class="brand-dot"></div>
  <div class="card-back-url">www.morvello-wellform.de</div>
</section>

</body>
</html>
```